Ironbark & Vale Construction and Developments business cards

A business card with watermark background (construction work)

Home improvement projects
House renovations
Bathroom and kitchen renovations
House extensions
New builds and granny flats

Director Tomas Verhoeven
(Phone number)
tomas@ivkbuilds.com.au
(Instagram logo) ivk_builds

```html
<!DOCTYPE html>
<html lang="en">
<head>
<meta charset="utf-8">
<title>Ironbark &amp; Vale – Business Cards</title>
<link rel="stylesheet" href="https://fonts.googleapis.com/css2?family=Open+Sans:wght@400&family=Montserrat:wght@400;500;600&display=swap">
<style>
  :root {
    --stage: #2a2a2a;
    --brand-blue: #3a7cc4;
    --brand-blue-deep: #2f6fb8;
    --card-white: #ffffff;
    --ink: #3a3a3a;
    --text-light: #ffffff;
  }
  * { box-sizing: border-box; margin: 0; padding: 0; }
  html, body { width: 1200px; height: 624px; overflow: hidden; }
  body { background: var(--stage); position: relative; font-family: "Open Sans", sans-serif; }

  .card {
    position: absolute; top: 176px; width: 476px; height: 286px; overflow: hidden;
  }
  .card--back { left: 100px; background: var(--brand-blue); }
  .card--front { left: 624px; background: var(--card-white); }

  .card__photo { position: absolute; inset: 0; }
  .card--back .card__photo {
    background: linear-gradient(120deg, rgba(30,80,150,0.35), rgba(80,140,210,0.15) 60%, rgba(30,80,150,0.25));
  }
  .card--front .card__photo {
    background: linear-gradient(115deg, #f3f3f3 0%, #e4e4e4 45%, #ececec 70%, #f6f6f6 100%);
  }

  .services { position: absolute; left: 62px; top: 72px; list-style: none; }
  .services__item {
    display: flex; align-items: center; height: 16px; margin-bottom: 14.5px;
    color: var(--text-light); font-size: 15px; letter-spacing: 0.1px; white-space: nowrap;
  }
  .services__tick { width: 12px; height: 12px; margin-right: 15px; flex: none; }

  .name-tab {
    position: absolute; left: 0; top: 30px; height: 54px;
    background: var(--brand-blue-deep); border-radius: 0 0 16px 0;
    padding: 8px 20px 0 35px; color: var(--text-light); font-family: "Montserrat", sans-serif;
    white-space: nowrap;
  }
  .name-tab__name { font-size: 19px; font-weight: 600; line-height: 23px; }
  .name-tab__title { font-size: 12px; font-weight: 400; line-height: 15px; }

  .company {
    position: absolute; left: 294px; top: 70px; width: 160px; text-align: center;
    display: flex; flex-direction: column; align-items: center; gap: 8px;
  }
  .company__mark { width: 14px; height: 14px; background: var(--brand-blue-deep); border-radius: 50%; }
  .company__name {
    font-family: "Montserrat", sans-serif; font-weight: 500; color: var(--brand-blue-deep);
    font-size: 15px; line-height: 18px;
  }
  .company__name small { display: block; font-size: 9px; letter-spacing: 1.5px; line-height: 14px; text-transform: uppercase; }

  .contacts {
    position: absolute; left: 35px; top: 182px; height: 64px;
    border-left: 1px solid #6d6d6d; padding-left: 7px; list-style: none;
    font-family: "Montserrat", sans-serif; color: var(--ink); font-size: 13px;
  }
  .contacts__row { display: flex; align-items: center; height: 19px; white-space: nowrap; }
  .contacts__icon { width: 11px; height: 11px; margin-right: 7px; flex: none; }
</style>
</head>
<body>

<section class="card card--back" aria-label="Card back: services">
  <div class="card__photo" role="img" aria-label="Faint blue-toned photo of a builder at a house construction site"></div>
  <ul class="services">
    <li class="services__item"><svg class="services__tick" viewBox="0 0 12 12"><path d="M1 7 L4.5 10.5 L11 1" fill="none" stroke="#fff" stroke-width="1.4"/></svg>Home improvement projects</li>
    <li class="services__item"><svg class="services__tick" viewBox="0 0 12 12"><path d="M1 7 L4.5 10.5 L11 1" fill="none" stroke="#fff" stroke-width="1.4"/></svg>House renovations</li>
    <li class="services__item"><svg class="services__tick" viewBox="0 0 12 12"><path d="M1 7 L4.5 10.5 L11 1" fill="none" stroke="#fff" stroke-width="1.4"/></svg>Bathroom and kitchen renovations</li>
    <li class="services__item"><svg class="services__tick" viewBox="0 0 12 12"><path d="M1 7 L4.5 10.5 L11 1" fill="none" stroke="#fff" stroke-width="1.4"/></svg>House extensions</li>
    <li class="services__item"><svg class="services__tick" viewBox="0 0 12 12"><path d="M1 7 L4.5 10.5 L11 1" fill="none" stroke="#fff" stroke-width="1.4"/></svg>New builds and granny flats</li>
  </ul>
</section>

<section class="card card--front" aria-label="Card front: contact">
  <div class="card__photo" role="img" aria-label="Faint greyscale photo of a builder showing a couple a house under construction"></div>

  <div class="name-tab">
    <p class="name-tab__name">Tomas Verhoeven</p>
    <p class="name-tab__title">Director</p>
  </div>

  <div class="company">
    <span class="company__mark"></span>
    <p class="company__name">Ironbark &amp; Vale<small>Construction and Developments</small></p>
  </div>

  <ul class="contacts">
    <li class="contacts__row">
      <svg class="contacts__icon" viewBox="0 0 12 12"><circle cx="6" cy="6" r="6" fill="#2f6fb8"/><path d="M3.6 3.2 L4.8 3 L5.4 4.6 L4.7 5.2 Q5.4 6.7 6.8 7.3 L7.4 6.6 L9 7.2 L8.8 8.4 Q5 8.6 3.6 3.2Z" fill="#fff"/></svg>104-555-872
    </li>
    <li class="contacts__row">
      <svg class="contacts__icon" viewBox="0 0 12 12"><circle cx="6" cy="6" r="6" fill="#2f6fb8"/><rect x="3" y="4" width="6" height="4.2" fill="#fff"/><path d="M3 4 L6 6.4 L9 4" fill="none" stroke="#2f6fb8" stroke-width="0.8"/></svg>tomas@ivkbuilds.com.au
    </li>
    <li class="contacts__row">
      <svg class="contacts__icon" viewBox="0 0 12 12"><circle cx="6" cy="6" r="6" fill="#2f6fb8"/></svg>ivk_builds
    </li>
  </ul>
</section>

</body>
</html>
```